Web Design Project - Shipping Industry

Goals and Objectives
The objective of the new website is to create a more modern look and feel. The site will also allow for a more effective means of communicating with members while providing the public with information and developments in the local, regional and international shipping industry.
Scope
The website will highlight the history of the organisation inclusive of text and photographs. It will take visitors through the years from beginning to present. Information on the history of the shipping industry will also be included.
It will feature current articles on the organisation, its members and stakeholders in the shipping industry. Member information as well as pertinent details regarding the organisation’s subsidiaries will be documented for the website.
Information as it relates to shipping statistics, case studies, laws and regulations, international treaties and trade documents, shipping terms, careers in shipping, job opportunities, training opportunities, information for shippers including port listing and trade lanes will be main features of the content for the website.
The Association’s community involvement, industry calendar events and related links relevant industry members will also be featured.
Target Market
• The General Public;
• Members of the organization;
• Shipping Industry Stakeholders (local, regional and international);
• Tertiary students conducting research.
• Potential employees
• Potential Business Partners
Best Practice Bench Marketing
The following websites are being looked at:
• Korvel Quays - http://www.korvelquays.example/ (preferred look)
• Tidewell Shipping Association - http://www.twa-ships.example/ (like image transition on main page)
• Brolund - http://www.brolund.example (professional look)
• KHW - http://www.kelharbours.example (preferred color: blue in logo)
• Vendlo - http://www.vendlo.example/electronics/tv-video-audio/ (preferred look for links page: image + short text below + visit site link)
Expected Result
• 3 - 5 pages which must include: [1] main page [2] standard page [3] links page
Target Market(s)
The General Public; Members of the organization; Shipping Industry Stakeholders (local, regional and international); Tertiary students conductin
Industry/Entity Type
Shipping

```html
<!DOCTYPE html>
<html lang="en">
<head>
<meta charset="utf-8">
<title>The Kelharbour Shipping Association</title>
<link rel="stylesheet" href="https://fonts.googleapis.com/css2?family=Arimo:wght@400;700&family=Crimson+Text&family=Varela+Round&display=swap">
<style>
:root{
  --royal:#0d3a9c;
  --royal-deep:#08277a;
  --brand:#1a48a8;
  --page:#f3f4f6;
  --text:#333;
  --muted:#666;
  --news-green:#5f8a3a;
  --line:#b8b8b8;
  --btn-top:#2f6fd6;
  --btn-bottom:#0e3fa6;
}
*{box-sizing:border-box;margin:0;padding:0}
html,body{width:1200px;height:1027px;overflow:hidden}
body{position:relative;background:radial-gradient(ellipse at 50% 30%,#2a5cc4 0%,var(--royal) 55%,var(--royal-deep) 100%);font-family:Arimo,Arial,sans-serif;color:var(--text)}
.abs{position:absolute}
.page{left:195px;top:0;width:805px;height:973px;background:var(--page)}
.brand-mark{left:242px;top:22px;width:36px;height:36px;border-radius:50%;background:var(--brand)}
.brand-name{left:313px;top:26px;font-family:"Crimson Text",Georgia,serif;font-size:23px;color:var(--brand);white-space:nowrap}
.search{left:782px;top:35px;width:168px;height:19px;display:flex}
.search input{flex:1;min-width:0;border:1px solid #c9c9c9;background:#eee;font:italic 9px Arimo,Arial,sans-serif;color:#999;padding-left:10px}
.search span{width:23px;background:var(--brand);display:flex;align-items:center;justify-content:center}
.nav{left:243px;top:74px;width:706px;height:23px;background:#e9eaec;display:flex;align-items:center;justify-content:space-between;padding-right:10px;font-family:"Varela Round",Arial,sans-serif;font-size:9.5px;color:#333;white-space:nowrap}
.nav a{text-decoration:none;color:inherit;padding:0 15px 0 0;height:14px;display:flex;align-items:center;border-right:1px solid #c7c7c7;white-space:nowrap}
.nav a:last-child{border:none;padding:0}
.nav a.active{background:var(--brand);color:#fff;height:23px;border:none;padding:0 20px}
.hero{left:245px;top:114px;width:704px;height:355px;background:linear-gradient(180deg,#c9d3dc 0%,#b4705e 40%,#7d6a66 70%,#5d6f86 100%);clip-path:polygon(0 85px,83px 0,100% 0,100% 225px,591px 100%,0 100%)}
.hero-dots{left:889px;top:424px;display:flex;gap:8px}
.dot{width:10px;height:10px;border-radius:50%;background:#aaa}
.dot.on{background:#111}
.thumb{width:108px;height:71px;background:linear-gradient(135deg,#dfe6ee,#9fb3c8);border:1px solid #bbb}
.caption{width:140px;text-align:center;font-size:10.5px;line-height:12px;color:var(--brand)}
.dash{height:0;border-top:1px dashed var(--line)}
.head{font-family:"Varela Round",Arial,sans-serif;color:var(--brand);white-space:nowrap;font-weight:400}
.news-title{left:244px;top:671px;font-family:"Varela Round",Arial,sans-serif;font-size:13px;color:var(--news-green);white-space:nowrap}
.news-title small{font-family:Arimo,Arial,sans-serif;font-size:9px;color:var(--muted);margin-left:6px}
.news-body{left:244px;top:691px;width:420px;font-size:10.2px;line-height:15.4px}
.link{font-size:10.5px;color:var(--brand);text-decoration:underline}
.news-dots{left:606px;top:742px;display:flex;gap:6px}
.news-dots .dot{width:7px;height:7px}
.news-dots .dot.on{background:var(--brand)}
.about{left:694px;top:514px;width:254px;font-size:10.3px;line-height:15.4px;hyphens:auto}
.about p+p{margin-top:15.4px}
.social{top:803px;width:36px;height:22px;transform:skewY(-8deg);border-radius:3px}
.address{left:441px;top:797px;font-size:9.5px;line-height:13.8px;color:#222;font-style:normal}
.member-box{left:693px;top:785px;width:256px;height:61px;border:1px solid #bfc3c9;background:#f7f7f8}
.member-photo{left:701px;top:788px;width:70px;height:57px;background:linear-gradient(135deg,#e4e4e4,#7a7f88)}
.partners{left:239px;top:869px;width:710px;height:75px;background:linear-gradient(180deg,#e8e9ec,#dcdee2)}
.partner{top:897px;font-weight:700;font-size:13px;color:var(--brand);white-space:nowrap}
.footer-copy{left:198px;top:990px;font-size:9px;color:#dde4f5}
.footer-mark{left:697px;top:985px;width:26px;height:26px;border-radius:50%;background:#c9d6f2}
.footer-name{right:203px;top:987px;font-family:"Crimson Text",Georgia,serif;font-size:17px;color:#dde4f5;white-space:nowrap}
.veil{left:0;top:0;width:1200px;height:1027px;background:rgba(255,255,255,.2)}
.modal{left:400px;top:141px;width:434px;height:223px;background:#fff;box-shadow:0 0 18px rgba(0,0,0,.35)}
.modal .title{left:23px;top:14px;font-size:14.5px}
.modal .close{left:412px;top:12px;font-size:13px;color:var(--brand)}
.modal .photo{left:18px;top:48px;width:165px;height:144px;background:linear-gradient(135deg,#f4f4f4,#7b7f88 60%,#2c2f36)}
.modal label{font-size:10.5px;color:var(--brand)}
.modal .field{left:208px;width:204px;height:22px;border:1px solid #cfcfcf;background:linear-gradient(#f4f4f4,#fff)}
.modal .forgot{left:212px;top:174px;font-size:9.5px;color:#222;white-space:nowrap}
.modal .login{left:343px;top:167px;width:69px;height:22px;background:linear-gradient(var(--btn-top),var(--btn-bottom));color:#fff;font-family:"Varela Round",Arial,sans-serif;font-size:11px;display:flex;align-items:center;justify-content:center}
</style>
</head>
<body>
<div class="abs page"></div>

<header>
  <div class="abs brand-mark"></div>
  <div class="abs brand-name">The Kelharbour Shipping Association</div>
  <div class="abs search"><input value="Search" aria-label="Search"><span><svg width="10" height="10" viewBox="0 0 10 10"><circle cx="4" cy="4" r="3" fill="none" stroke="#fff" stroke-width="1.4"/><line x1="6.2" y1="6.2" x2="9" y2="9" stroke="#fff" stroke-width="1.6"/></svg></span></div>
  <nav class="abs nav">
    <a class="active">HOME</a><a>ABOUT US</a><a>PRODUCTS</a><a>SERVICES</a><a>NEWS</a><a>SUPPORT</a><a>PARTNERS</a><a>CUSTOMERS</a><a>CONTACT</a>
  </nav>
</header>

<div class="abs hero" role="img" aria-label="Container port with red gantry cranes, stacked containers and harbour water"></div>
<div class="abs hero-dots"><span class="dot on"></span><span class="dot"></span><span class="dot"></span></div>

<section>
  <div class="abs thumb" style="left:244px;top:494px" role="img" aria-label="Team meeting in an office"></div>
  <div class="abs thumb" style="left:394px;top:494px" role="img" aria-label="Help desk staff at work"></div>
  <div class="abs thumb" style="left:542px;top:494px" role="img" aria-label="Workers in hard hats on site"></div>
  <div class="abs caption" style="left:228px;top:580px">IT Management<br>Services</div>
  <div class="abs caption" style="left:378px;top:580px">Help Desk</div>
  <div class="abs caption" style="left:526px;top:580px">Disaster Recovery<br>&amp; Business Continuity</div>
</section>

<div class="abs dash" style="left:241px;top:626px;width:419px"></div>

<section>
  <h2 class="abs head" style="left:244px;top:645px;font-size:15.5px">LATEST NEWS</h2>
  <div class="abs news-title">Lorem ipsum dolor sit amet<small>19th May 2012</small></div>
  <p class="abs news-body">Nummy nibh euismod tincidunt ut laoreet dolore magna aliquam erat volutpat. Ut wisi enim ad minim veniam, quis nostrud exerci tation ullamcorper wisi enim ad minim veniam.</p>
  <a class="abs link" style="left:244px;top:735px">View All</a>
  <div class="abs news-dots"><span class="dot on"></span><span class="dot"></span><span class="dot"></span></div>
</section>

<section>
  <h2 class="abs head" style="left:692px;top:493px;font-size:11px">THE KELHARBOUR SHIPPING ASSOCIATION</h2>
  <div class="abs about" lang="en">
    <p>Registered as a Trade Union, one of the primary functions of the Association is the manangement of certain categories of labour on the Port. In addition, the Association acts on behalf of its members in initiatives to advance industrial relations, training, security, information technology, and to establish uniform standards and rates of remuneration for port labour within the Maritime Sector.</p>
    <p>The Association, like other Trade Associations, has a strong advocacy and lobbying remit, and liaises with Government agencies and bodies, as well as other private sector organizations to ensure the continued development of the Shipping Industry in the island.</p>
  </div>
  <a class="abs link" style="left:694px;top:742px;color:var(--news-green)">Read More</a>
</section>

<div class="abs dash" style="left:241px;top:770px;width:419px"></div>
<div class="abs dash" style="left:693px;top:770px;width:253px"></div>

<div class="abs social" style="left:248px;background:#2d4f96"></div>
<div class="abs social" style="left:303px;background:#2aa1cf"></div>
<div class="abs social" style="left:362px;background:#e4782a"></div>
<address class="abs address">Meridan Shipping, 12 Quayside Road,<br>Harbour West, Port Alder 9. West Indies<br>Email: info@meridanports.example</address>

<div class="abs member-box"></div>
<div class="abs member-photo" role="img" aria-label="Two engineers in hard hats reviewing plans"></div>
<div class="abs head" style="left:780px;top:803px;font-size:14px">MEMBER LOGIN AREA</div>
<div class="abs" style="left:780px;top:821px;font-size:8px;color:#333">Lorem ipsum dolor sit amet, consectetur</div>

<section>
  <div class="abs partners"></div>
  <div class="abs head" style="left:243px;top:893px;font-size:12.5px;line-height:15px">OUR<br>PARTNERS</div>
  <svg class="abs" style="left:330px;top:898px" width="12" height="18" viewBox="0 0 12 18"><path d="M10 1 2 9l8 8" fill="none" stroke="#b0b3b8" stroke-width="2.5"/></svg>
  <svg class="abs" style="left:924px;top:898px" width="12" height="18" viewBox="0 0 12 18"><path d="M2 1l8 8-8 8" fill="none" stroke="#b0b3b8" stroke-width="2.5"/></svg>
  <div class="abs partner" style="left:367px">Northbay Marine</div>
  <div class="abs partner" style="left:513px">Corlan Wharves</div>
  <div class="abs partner" style="left:653px">Tidelane Freight</div>
  <div class="abs partner" style="left:792px">Ostra Shipping</div>
</section>

<footer>
  <div class="abs footer-copy">© The Kelharbour Shipping Association 2012, All Right Reserved</div>
  <div class="abs footer-mark"></div>
  <div class="abs footer-name">The Kelharbour Shipping Association</div>
</footer>

<div class="abs veil"></div>

<div class="abs modal" role="dialog" aria-label="Member login">
  <h2 class="abs head title">MEMBER LOGIN</h2>
  <span class="abs close">✕</span>
  <div class="abs photo" role="img" aria-label="Two engineers in hard hats, one pointing upward"></div>
  <label class="abs" style="left:207px;top:64px">Username</label>
  <div class="abs field" style="top:81px"></div>
  <label class="abs" style="left:208px;top:112px">Password</label>
  <div class="abs field" style="top:132px"></div>
  <span class="abs forgot">Forgot your password?</span>
  <span class="abs login">LOGIN</span>
</div>
</body>
</html>
```